Webdesign mit Grundfarbe Weinrot für allgemeine Steuerberatung
Zielgruppe
Allgemeine Steuerberatung. Zielgruppe ist breit gefächert, allerdings soll die Webseite eher den Jungunternehmer ansprechen.
Aufgabenstellung
Die Grundfarbe sollte weinrot sein.

```html
<!DOCTYPE html>
<html lang="de">
<head>
<meta charset="utf-8">
<title>Steuerberatung K1vra</title>
<link href="https://fonts.googleapis.com/css2?family=Raleway:wght@300;400;500;600;700&display=swap" rel="stylesheet">
<style>
:root{
  --wine:#4e0016;
  --wine-mid:#8f2745;
  --wine-btn:#9a2a49;
  --wine-caption:rgba(128,40,62,.82);
  --text:#333;
  --text-soft:#555;
  --bg-soft:#f7f7f7;
  --white:#fff;
  --bar:#1c1c1c;
}
*{box-sizing:border-box;margin:0;padding:0}
html,body{width:1200px;height:2318px;overflow:hidden;background:var(--white);font-family:'Raleway',sans-serif;color:var(--text)}
.page{position:relative;width:1200px;height:2318px}
.abs{position:absolute}

.site-header{left:0;top:0;width:1200px;height:81px;background:var(--white)}
.brand{left:246px;top:14px;height:60px;display:flex;align-items:center;gap:8px;color:var(--wine);font-weight:600;font-size:20px}
.brand-mark{width:14px;height:14px;background:var(--wine)}
.brand small{display:block;font-size:11px;font-weight:500;color:var(--wine)}
.contact-line{left:821px;top:14px;font-size:11px;color:var(--wine);font-weight:500}
.contact-line span{display:block;font-size:7px;color:#777;margin-left:11px;font-weight:400}
.main-nav{top:60px;left:0;width:1200px;font-size:12.5px}
.main-nav a{position:absolute;text-decoration:none;color:#777}
.main-nav a.active{color:var(--wine);font-weight:600}

.hero{left:0;top:81px;width:1200px;height:300px;background:linear-gradient(90deg,#dcd6cc 0%,#d9cfc0 40%,#c9a682 55%,#c47a6d 70%,#e1d8cb 100%)}
.hero-caption{left:239px;top:205px;min-width:301px;height:77px;background:var(--wine-caption);color:var(--white);padding:9px 17px;line-height:1.15;white-space:nowrap}
.hero-caption .light{font-weight:300;font-size:26px;display:block}
.hero-caption .bold{font-weight:600;font-size:26px;display:block}
.slider-arrow{top:202px;width:28px;height:59px;background:rgba(235,235,235,.85);display:flex;align-items:center;justify-content:center}

.about-photo{left:241px;top:453px;width:303px;height:205px;background:linear-gradient(135deg,#e3e6ec,#b9bfcb 50%,#8b94a8)}
.about-text{left:572px;top:455px;width:384px}
.about-text h2{font-weight:400;font-size:20px;margin-bottom:14px;color:#222}
.about-text p{font-size:10px;line-height:16.4px;color:var(--text-soft);margin-bottom:16px}

.services{left:0;top:727px;width:1200px;height:372px;background:var(--bg-soft)}
.section-title{width:1200px;text-align:center;font-weight:500;font-size:19px;color:#222}
.section-sub{width:1200px;text-align:center;font-size:10px;letter-spacing:.5px;color:#555}
.service{width:170px;text-align:center}
.service svg{display:block;margin:0 auto}
.service h3{margin-top:22px;font-size:12.5px;font-weight:500;color:var(--wine)}
.service p{margin-top:16px;font-size:10px;line-height:16.4px;color:#666}
.service b,.news-card b{color:var(--wine)}

.cta{left:0;top:1099px;width:1200px;height:241px;background:var(--wine);color:var(--white);text-align:center}
.cta h2{position:absolute;top:52px;width:1200px;font-weight:500;font-size:23px;letter-spacing:.8px}
.cta p{position:absolute;top:94px;width:1200px;font-size:12.5px;line-height:18px}
.btn{display:flex;align-items:center;justify-content:center;font-size:10px;font-weight:500}
.btn-light{left:530px;top:158px;width:152px;height:33px;background:#ddd;color:#333}

.news{left:0;top:1340px;width:1200px;height:501px;background:var(--bg-soft)}
.news-card{width:228px;height:253px;background:var(--white);box-shadow:0 1px 3px rgba(0,0,0,.06)}
.news-card .thumb{height:97px}
.news-card h3{padding:12px 7px 0;font-size:12.5px;font-weight:500;line-height:16.5px;color:#222}
.news-card p{padding:9px 7px 0;font-size:9.5px;line-height:16.4px;color:#666}
.btn-wine{left:528px;top:1759px;width:153px;height:33px;background:var(--wine-btn);color:var(--white)}

.map{left:0;top:1841px;width:1200px;height:275px;background:linear-gradient(120deg,#e8e8e8,#dedede 60%,#d6e8d0)}

.site-footer{left:0;top:2116px;width:1200px;height:177px;background:var(--wine);color:var(--white)}
.site-footer h4{font-size:9px;font-weight:700;margin-bottom:6px}
.site-footer p,.site-footer li{font-size:8px;line-height:13.3px;list-style:none}
.footer-bar{left:0;top:2293px;width:1200px;height:25px;background:var(--bar);color:var(--white);font-size:7.5px;font-weight:700;padding:7px 0 0 237px}
</style>
</head>
<body>
<div class="page">

<header class="site-header abs">
  <div class="brand abs"><span class="brand-mark"></span><div>K1vra<small>Steuerberaterin</small></div></div>
  <div class="contact-line abs">
    <svg width="9" height="9" viewBox="0 0 24 24"><path fill="#4e0016" d="M6.6 10.8a15 15 0 006.6 6.6l2.2-2.2a1 1 0 011-.25 11.4 11.4 0 003.6.57 1 1 0 011 1V20a1 1 0 01-1 1A17 17 0 013 4a1 1 0 011-1h3.5a1 1 0 011 1c0 1.25.2 2.450.57 3.57a1 1 0 01-.25 1z"/></svg>
    +49 (0)6400-555120
    <span>Mo-Do: 8:00 - 16:00 | Fr. 8:00 -12:30</span>
  </div>
  <nav class="main-nav abs">
    <a class="active" style="left:498px">Start</a>
    <a style="left:555px">Leistungen</a>
    <a style="left:650px">Über uns</a>
    <a style="left:733px">Aktuelles</a>
    <a style="left:816px">Kontakt</a>
  </nav>
</header>

<section class="hero abs" role="img" aria-label="Foto einer lächelnden Beraterin mit Brille">
</section>
<div class="hero-caption abs"><span class="light">Wilkommen bei der</span><span class="bold">Steuerberatung K1vra</span></div>
<div class="slider-arrow abs" style="left:34px"><svg width="12" height="16" viewBox="0 0 12 16"><path d="M9 2L3 8l6 6" fill="none" stroke="#666" stroke-width="2.5"/></svg></div>
<div class="slider-arrow abs" style="left:1137px"><svg width="12" height="16" viewBox="0 0 12 16"><path d="M3 2l6 6-6 6" fill="none" stroke="#666" stroke-width="2.5"/></svg></div>

<div class="about-photo abs" role="img" aria-label="Foto von zwei Mitarbeiterinnen im Büro"></div>
<div class="about-text abs">
  <h2>Über uns</h2>
  <p>Meine Kanzlei berät seit deren Gründung im Jahre 2003 Freiberufler, Gewerbetreibende, Kapitalgesellschaften, Personengesellschaften aus den verschiedensten Branchen sowie gemeinnützige Organisationen. Ebenso unterstützen wir gerne Existenzgründer und nebenberuflich Tätige, wie auch Arbeitnehmer, Vermieter und Rentner.</p>
  <p>Mein Team aus erfahrenen Steuerfachangestellten und ich freuen uns, Ihnen kompetent und individuell auf Ihre persönlichen Bedürfnisse abgestimmt, bei Ihren steuerlichen Angelegenheiten zu helfen!</p>
</div>

<section class="services abs">
  <h2 class="section-title abs" style="top:52px">Leistungen</h2>
  <p class="section-sub abs" style="top:79px">Leistungsspektrum unserer Steuerberatungskanzlei in der Übersicht</p>

  <div class="service abs" style="left:239px;top:133px">
    <svg width="52" height="52" viewBox="0 0 52 52" fill="none" stroke="#8f2745" stroke-width="3"><rect x="4" y="4" width="40" height="44"/><rect x="9" y="9" width="40" height="40" fill="#fff"/><path d="M16 20h26M16 26h26M16 32h26M16 38h26"/></svg>
    <h3>Buchhaltung</h3>
    <p>Lorem ipsum dolor sit amet, consetetur sadipscing elitr, sed diam nonumy eirmod tempor invidunt ut labore et dolore magna aliquyam erat, sed diam voluptua. <b>»</b></p>
  </div>
  <div class="service abs" style="left:423px;top:133px">
    <svg width="52" height="52" viewBox="0 0 52 52" fill="none" stroke="#8f2745" stroke-width="3"><path d="M14 4h34v44H6V24h8z"/><path d="M14 24v24M20 14h22M20 22h22M20 30h22M20 38h22"/></svg>
    <h3>Lohnabrechnungen</h3>
    <p>Lorem ipsum dolor sit amet, consetetur sadipscing elitr, sed diam nonumy eirmod tempor invidunt ut labore et dolore magna aliquyam erat, sed diam voluptua. <b>»</b></p>
  </div>
  <div class="service abs" style="left:606px;top:133px">
    <svg width="52" height="52" viewBox="0 0 52 52" fill="none" stroke="#8f2745" stroke-width="3"><rect x="6" y="6" width="40" height="44"/><path d="M30 2v16a4 4 0 008 0V4M12 18h14M12 26h28M12 34h28M12 42h20"/></svg>
    <h3>Jahresabschluss</h3>
    <p>Lorem ipsum dolor sit amet, consetetur sadipscing elitr, sed diam nonumy eirmod tempor invidunt ut labore et dolore magna aliquyam erat, sed diam voluptua. <b>»</b></p>
  </div>
  <div class="service abs" style="left:790px;top:133px">
    <svg width="52" height="52" viewBox="0 0 52 52" fill="none" stroke="#8f2745" stroke-width="3"><path d="M4 4h16l4 6h24v38H4z"/><path d="M4 12h44"/><circle cx="28" cy="29" r="6"/><path d="M24 33l-7 7"/></svg>
    <h3>Steuererklärungen</h3>
    <p>Lorem ipsum dolor sit amet, consetetur sadipscing elitr, sed diam nonumy eirmod tempor invidunt ut labore et dolore magna aliquyam erat, sed diam voluptua. <b>»</b></p>
  </div>
</section>

<section class="cta abs">
  <h2>Können wir Ihnen weiterhelfen?</h2>
  <p>Gerne beantworten wie Ihre Fragen und vereinbaren mir Ihnen<br>einen Termin. Sie können uns anrufen oder uns eine Nachricht schicken.</p>
  <div class="btn btn-light abs">KONTAKTFORMULAR</div>
</section>

<section class="news abs">
  <h2 class="section-title abs" style="top:56px">Neuigkeiten</h2>
  <p class="section-sub abs" style="top:88px">Aktuelle Meldungen zu diversen Steuerthemen</p>

  <article class="news-card abs" style="left:240px;top:132px">
    <div class="thumb" role="img" aria-label="Foto einer Hand am Taschenrechner" style="background:linear-gradient(135deg,#f1f1f1,#cfcfcf 60%,#6a6a6a)"></div>
    <h3>Lohnsteuer: Aktuelles zum Dienstwagen</h3>
    <p style="padding-top:17px">Die Privatnutzung von Dienstwagen ist für viele Arbeitnehmer ein attraktiver Lohnbestandteil, obgleich sich dieser Vorteil in aller Regel steuererhöhend auswirkt. In einem neuen Schreiben <b>»</b></p>
  </article>
  <article class="news-card abs" style="left:486px;top:132px">
    <div class="thumb" role="img" aria-label="Foto einer Tasse auf einem Buch am Fenster" style="background:linear-gradient(135deg,#6b4328,#c79a5a 50%,#6f8a4a)"></div>
    <h3>Abschreibung bei „Arbeitswohnung“ im Miteigentum eines Ehepaars</h3>
    <p style="padding-top:0">Die Kosten eines außerhäuslichen Arbeitszimmers lassen sich in unbeschränkter Höhe absetzen - selbst wenn dort nicht der Tätigkeitsmittelpunkt liegt. In einem Streitfall vor dem Bundesfinanzhof <b>»</b></p>
  </article>
  <article class="news-card abs" style="left:733px;top:132px">
    <div class="thumb" role="img" aria-label="Foto eines älteren Paares beim Spaziergang" style="background:linear-gradient(135deg,#5f6a3c,#b99868 50%,#3f3a30)"></div>
    <h3>Kein Lohnzufluss bei Gehaltsumwandlung für vorzeitigen Ruhestand</h3>
    <p style="padding-top:0">Bei der Einrichtung eines Zeitwertkontos kann der Arbeitnehmer darauf Teile seines fälligen Arbeitslohns „ansparen“, um diesen dann in einer späteren Freistellungsphase ausgezahlt zu bekommen. <b>»</b></p>
  </article>
</section>
<div class="btn btn-wine abs">WEITERE NEUIGKEITEN</div>

<div class="map abs" role="img" aria-label="Stadtplan mit Standort der Kanzlei"></div>

<footer class="site-footer abs">
  <div class="abs" style="left:237px;top:26px;width:270px">
    <h4>ÜBER UNS</h4>
    <p>Lorem ipsum dolor sit amet, consetetur sadipscing elitr, sed diam nonumy eirmod tempor invidunt ut labore et dolore magna aliquyam erat, sed diam voluptua. At vero eos et accusam et justo duo dolores et ea rebum. Stet clita kasd gubergren, no sea takimata sanctus est Lorem ipsum dolor sit amet. Lorem ipsum dolor sit amet, consetetur sadipscing elitr, sed diam nonumy eirmod tempor invidunt ut labore et dolore magna aliquyam erat, sed diam voluptua.</p>
  </div>
  <div class="abs" style="left:595px;top:26px">
    <h4>SITEMAP</h4>
    <ul><li>» Leistungen</li><li>» Über uns</li><li>» Aktuelles</li><li>» Kontakt</li></ul>
    <h4 style="margin-top:30px">RECHTLICHES</h4>
    <ul><li>» IMPRESSUM</li><li>» DATENSCHUTZ</li></ul>
  </div>
</footer>
<div class="footer-bar abs">Copyright © 2019 - Steuerberatung K1vra</div>

</div>
</body>
</html>
```